Financial Advisor needs a BOLD Business Card

I need a business card that is professional, and is also eye-catching and memorable. I would like to include my photo (several different professional photos have been uploaded). Preferred primary color is blue, or green, or dark purple. The final design should have a modern/contemporary look while communicating a professional image.

Target Market(s)

Individual Investors and Small Business Owners

Industry/Entity Type

Business

Contact Information for Business Card

[side 1:] Dale Varkonen Financial Advisor 58217 Marlow Brook Rd., #240 St. Louis, MO 63975 (314) 555-0187 main (314) 555-0142 cell (314) 555-0169 fax dalev@qrmvbk.com [side 2:] Life Insurance | Retirement | Employee Benefits

Font styles to use
Serif
Sans Serif

Requirements
Must have
• [disclaimer, text can be 7-9 point:] Securities offered through the K.R. Capital Trading Company. Member BLUDA/TAVK. Nine Harbor Circle, Cincinnati, Ohio 45817. 513-555-0123. Investment Advisory Services offered through K.R. Portfolio Stewardship Company.
Nice to have
• Bright, Light & Airy feel on Side 1 with contact data, bold patterns, high color contrast, modern or 3D look
Should not have
• Any symbols referring to money (e.g. $)

```html
<!DOCTYPE html>
<html lang="en">
<head>
<meta charset="utf-8">
<title>Dale Varkonen – Business Card</title>
<link href="https://fonts.googleapis.com/css2?family=Roboto:wght@300;400&display=swap" rel="stylesheet">
<style>
  :root {
    --bg: #3a3b3f;
    --paper: #f7fafa;
    --navy: #23232f;
    --cyan: #3fc3e3;
    --ink: #2b2b33;
    --muted: #6a6d74;
    --photo-dark: #2a2622;
    --photo-mid: #5a4a44;
  }
  * { margin: 0; padding: 0; box-sizing: border-box; }
  html, body { width: 1200px; height: 960px; overflow: hidden; }
  body {
    background: var(--bg);
    font-family: "Roboto", sans-serif;
    color: var(--ink);
    position: relative;
  }
  .card {
    position: absolute;
    left: 250px;
    width: 700px;
    height: 400px;
    background: var(--paper);
    overflow: hidden;
    box-shadow: 0 12px 30px rgba(0,0,0,.35);
  }
  .card--services { top: 50px; }
  .card--contact { top: 510px; }

  .stripes { position: absolute; left: 0; right: 0; bottom: 0; height: 70px; }
  .stripes__navy { position: absolute; left: 0; right: 0; top: 0; height: 24px; background: var(--navy); }
  .stripes__cyan { position: absolute; left: 0; right: 0; top: 32px; bottom: 0; background: var(--cyan); }

  .services {
    position: absolute;
    left: 170px;
    top: 96px;
    list-style: none;
    font-weight: 300;
    font-size: 34px;
    line-height: 44px;
  }
  .services li { display: flex; align-items: center; }
  .services li:nth-child(2) { padding-left: 34px; }
  .services li:nth-child(3) { padding-left: 68px; }
  .services .bullet { color: var(--cyan); font-size: 26px; width: 34px; font-weight: 400; }

  .disclaimer {
    position: absolute;
    left: 40px;
    right: 40px;
    bottom: 84px;
    font-size: 10px;
    line-height: 14px;
    font-weight: 400;
    color: var(--muted);
  }

  .photo {
    position: absolute;
    left: 26px;
    top: 120px;
    width: 220px;
    height: 280px;
    background: linear-gradient(160deg, var(--photo-mid), var(--photo-dark) 60%);
  }
  .identity {
    position: absolute;
    right: 34px;
    top: 30px;
    text-align: right;
  }
  .identity__name { color: var(--cyan); font-weight: 300; font-size: 28px; }
  .identity__title { font-size: 14px; font-weight: 400; margin-top: 2px; margin-right: 36px; }

  .contacts {
    position: absolute;
    right: 26px;
    top: 108px;
    list-style: none;
    font-size: 16px;
    font-weight: 300;
    line-height: 30px;
    white-space: nowrap;
  }
  .contacts li { display: flex; justify-content: flex-end; align-items: center; gap: 14px; }
  .contacts svg { width: 18px; height: 18px; fill: var(--cyan); flex: none; }
</style>
</head>
<body>

<section class="card card--services">
  <ul class="services">
    <li><span class="bullet">✳</span>Life Insurance</li>
    <li><span class="bullet">✳</span>Retirement</li>
    <li><span class="bullet">✳</span>Employee Benefits</li>
  </ul>
  <p class="disclaimer">Securities offered through the K.R. Capital Trading Company. Member BLUDA/TAVK. Nine Harbor Circle, Cincinnati, Ohio 45817. 513-555-0123. Investment Advisory Services offered through K.R. Portfolio Stewardship Company.</p>
  <div class="stripes"><div class="stripes__navy"></div><div class="stripes__cyan"></div></div>
</section>

<section class="card card--contact">
  <div class="stripes"><div class="stripes__navy"></div><div class="stripes__cyan"></div></div>
  <div class="photo" role="img" aria-label="Portrait photo of the advisor in a dark suit"></div>

  <div class="identity">
    <div class="identity__name">Dale Varkonen</div>
    <div class="identity__title">Financial Advisor</div>
  </div>

  <ul class="contacts">
    <li>(314) 555-0187
      <svg viewBox="0 0 24 24"><path d="M3 9c0-3 4-5 9-5s9 2 9 5v2h-5V9H8v2H3z M6 12h12l2 8H4z"/></svg></li>
    <li>(314) 555-0142
      <svg viewBox="0 0 24 24"><path d="M7 2h10a1 1 0 0 1 1 1v18a1 1 0 0 1-1 1H7a1 1 0 0 1-1-1V3a1 1 0 0 1 1-1zm1 3v12h8V5z"/></svg></li>
    <li>(314) 555-0169
      <svg viewBox="0 0 24 24"><path d="M7 2h9v6H7z M3 9h18v11H3z M6 12v2h3v-2z"/></svg></li>
    <li>dalev@qrmvbk.com
      <svg viewBox="0 0 24 24"><path d="M2 5h20v14H2z M3 6l9 7 9-7" stroke="#f7fafa" stroke-width="1.5"/></svg></li>
    <li>58217 Marlow Brook Rd., #240 St. Louis, MO 63975
      <svg viewBox="0 0 24 24"><path d="M12 2a7 7 0 0 1 7 7c0 5-7 13-7 13S5 14 5 9a7 7 0 0 1 7-7zm0 4a3 3 0 1 0 0 6 3 3 0 0 0 0-6z"/></svg></li>
  </ul>
</section>

</body>
</html>
```